Web Design Project

We are a SaaS company that specializes in the thrift industry POS and inventory software. We want a clean and professional site that does NOT look like a template site.

*** A little more about our business -
We offer a SaaS (Software As A Service) for a Point Of Sale and inventory control product specifically for the Thrift / Second hand industry. The software allows them to process inventory, grade/rate it, create the barcoded tags. It the does the whole retail sale process. We also offer tie-ins to Pixelyard, Chirpnest and apple/droid mobile apps to support our customers thrift stores.

We need to in incorporate the look/feel and color scheme of our logo.

I would imagine possibly a HTML5 slideshow (3-5 slides) rotating on the home page showing screenshots, etc.

I am envisioning icons representing features of our product.

PLEASE ask questions, I am sure I have left out a ton.
Updates

Requirements
Must have
• I have attached a couple of our logo's with color options. It needs to flow with that.

I have also attached a screen shot of what I think might work. This DOESN'T suggest that is what I am looking for, just a sample.

I am thinking a home page and maybe one or two sub pages
***Update, I kind of like the following concept for one of the sub-pages
http://www.quotivex.example/estimate.html

There should also be a place to highlight Pixelyard and chirpnest.

It will be a bilingual / multilingual site, so take that into account
Should not have
• I don't want it to look like a template site. It should be clean and professional.

```html
<!DOCTYPE html>
<html lang="en">
<head>
<meta charset="utf-8">
<title>Tagwell – Thrift Store POS &amp; Inventory</title>
<link href="https://fonts.googleapis.com/css2?family=PT+Sans+Narrow:wght@400;700&family=Source+Sans+3:wght@400;600&family=Noto+Serif:ital@1&family=Open+Sans:wght@400&display=swap" rel="stylesheet">
<style>
:root{
  --header-bg:#2c3a45;
  --page-bg:#ececec;
  --brand:#1a9ad6;
  --nav-text:#333;
  --slide:#6b6b6b;
  --intro:#6e6e6e;
  --body:#3a3a3a;
  --footer-bg:#2e2e2e;
  --footer-deep:#242424;
  --footer-text:#a9a9a9;
  --heading-light:#d8d8d8;
  --tick:#8cc63f;
}
*{box-sizing:border-box;margin:0;padding:0}
html,body{width:1121px;height:1200px;overflow:hidden}
body{position:relative;background:var(--page-bg);font-family:"Open Sans",Verdana,sans-serif}
.site-header{position:absolute;left:0;top:0;width:1121px;height:101px;background:var(--header-bg)}
.brand{position:absolute;left:148px;top:34px;display:flex;align-items:center;gap:8px;font-family:"Source Sans 3",sans-serif;font-weight:600;font-size:30px;line-height:36px;color:var(--brand)}
.brand-mark{width:22px;height:22px;background:var(--brand);border-radius:3px}
.main-nav{position:absolute;left:577px;top:38px;width:393px;height:28px;background:linear-gradient(#fff,#e6e6e6);border-radius:5px;display:flex;align-items:center;justify-content:space-around;padding:0 8px}
.main-nav a{font-family:"PT Sans Narrow",sans-serif;font-size:17px;color:var(--nav-text);text-decoration:none;padding:0 12px;border-left:1px solid #ccc}
.main-nav a:first-child{border-left:none}
.main-nav a.active{background:#ddd;padding:3px 12px}
.slider{position:absolute;left:133px;top:101px;width:837px;height:354px;background:#fff;border-radius:0 0 6px 6px;box-shadow:0 2px 4px rgba(0,0,0,.12)}
.slide{position:absolute;left:13px;top:12px;width:812px;height:306px;background:var(--slide)}
.dots{position:absolute;left:13px;top:331px;display:flex;gap:4px}
.dots span{width:10px;height:10px;border-radius:50%;background:#ccc}
.dots span.on{background:#888}
.arrows{position:absolute;right:12px;top:327px;display:flex;gap:4px}
.arrows span{width:18px;height:18px;border-radius:50%;background:#c8c8c8}
.arrows span+span{background:#888}
.intro{position:absolute;left:132px;top:504px;width:840px;font-family:"Source Sans 3",sans-serif;font-size:23px;line-height:29px;color:var(--intro)}
.features{position:absolute;left:123px;top:626px;width:880px;display:flex}
.feature{width:220px;text-align:center}
.feature-art{width:54px;height:54px;margin:0 auto;border-radius:50%}
.feature h3{font-family:"PT Sans Narrow",sans-serif;font-weight:400;font-size:18.5px;line-height:22px;color:#333;margin-top:10px}
.feature p{font-size:11.3px;line-height:17.5px;color:var(--body);margin-top:5px;padding:0 18px;height:54px;overflow:hidden}
.btn{display:inline-block;margin-top:10px;width:103px;height:31px;line-height:31px;border-radius:4px;background:linear-gradient(#fff,#e8e8e8);box-shadow:0 1px 2px rgba(0,0,0,.3);font-family:"PT Sans Narrow",sans-serif;font-size:16.5px;color:#333}
.site-footer{position:absolute;left:0;top:852px;width:1121px;height:287px;background:var(--footer-bg);border-top:2px solid #1e1e1e}
.widget{position:absolute;top:18px}
.widget h4{display:flex;align-items:center;gap:8px;font-family:"PT Sans Narrow",sans-serif;font-weight:400;font-size:21px;color:var(--heading-light)}
.widget-icon{width:24px;height:24px;border-radius:3px}
.widget ul{list-style:none;margin-top:12px}
.widget li{display:flex;gap:14px;font-size:10.5px;line-height:17px;color:var(--footer-text);margin-bottom:14px}
.widget li svg{flex:none;margin-top:1px}
.archives li{margin-bottom:13.5px}
.chirp-box{margin-top:20px;width:245px;height:128px;background:var(--footer-deep);border-radius:5px;padding:10px 14px 0 16px;font-family:"Noto Serif",serif;font-style:italic;font-size:11.5px;line-height:17.5px;color:var(--footer-text)}
.bottom-bar{position:absolute;left:0;top:1139px;width:1121px;height:61px;background:var(--footer-deep)}
.copyright{position:absolute;left:192px;top:23px;font-size:11px;color:var(--footer-text)}
.social{position:absolute;left:780px;top:20px;display:flex;gap:9px}
.social span{width:20px;height:20px;border-radius:3px}
</style>
</head>
<body>
<header class="site-header">
  <div class="brand"><span class="brand-mark"></span>Tagwell</div>
  <nav class="main-nav">
    <a href="#">Home</a><a href="#" class="active">Blog</a><a href="#">Portfolio</a><a href="#">Services</a><a href="#">Contact</a>
  </nav>
</header>

<section class="slider">
  <div class="slide" role="img" aria-label="Screenshot of the Tagwell point of sale screen"></div>
  <div class="dots"><span></span><span class="on"></span><span></span><span></span></div>
  <div class="arrows"><span></span><span></span></div>
</section>

<p class="intro">Hi! Tagwell is point of sale and inventory software built for thrift and second hand stores. Process donations, grade and price each item, print tags and ring up every sale from one simple system, in the language your team speaks.</p>

<section class="features">
  <div class="feature">
    <div class="feature-art" style="border-radius:4px;background:linear-gradient(#8ab4f0,#5d8ee0)" role="img" aria-label="Inventory box icon"></div>
    <h3>Inventory</h3>
    <p>Process donated goods, grade and rate each item and track stock across all your stores.</p>
    <a class="btn">View Details</a>
  </div>
  <div class="feature">
    <div class="feature-art" style="background:radial-gradient(circle at 35% 35%,#9fd86b,#3a7fd0)" role="img" aria-label="Globe icon"></div>
    <h3>Point of Sale</h3>
    <p>Fast checkout for busy thrift counters, with discounts, daily reports and many languages.</p>
    <a class="btn">View Details</a>
  </div>
  <div class="feature">
    <div class="feature-art" style="border-radius:4px;background:linear-gradient(#a6d83a,#6fa81c)" role="img" aria-label="Shopping basket icon"></div>
    <h3>Tag Printing</h3>
    <p>Create priced, barcoded tags in seconds and scan them straight back in at the register.</p>
    <a class="btn">View Details</a>
  </div>
  <div class="feature">
    <div class="feature-art" style="background:radial-gradient(circle,#ececec 30%,#f0642a 32%,#e85a20 70%,#ddd 72%)" role="img" aria-label="Support ring icon"></div>
    <h3>Pixelyard &amp; Apps</h3>
    <p>Share new arrivals on Pixelyard and Chirpnest and reach shoppers on phone apps.</p>
    <a class="btn">View Details</a>
  </div>
</section>

<footer class="site-footer">
  <div class="widget" style="left:192px;width:260px">
    <h4><span class="widget-icon" style="background:#eee" role="img" aria-label="Notepad icon"></span>Recent Posts</h4>
    <ul>
      <li><svg width="14" height="12"><path d="M1 6l4 4 8-9" stroke="var(--tick)" stroke-width="2.5" fill="none"/></svg>Grading donations for faster pricing</li>
      <li><svg width="14" height="12"><path d="M1 6l4 4 8-9" stroke="var(--tick)" stroke-width="2.5" fill="none"/></svg>Five ways tag printing saves thrift staff hours each week</li>
      <li><svg width="14" height="12"><path d="M1 6l4 4 8-9" stroke="var(--tick)" stroke-width="2.5" fill="none"/></svg>Tagwell now speaks Spanish, French and German</li>
      <li><svg width="14" height="12"><path d="M1 6l4 4 8-9" stroke="var(--tick)" stroke-width="2.5" fill="none"/></svg>Sell new arrivals on Pixelyard</li>
      <li><svg width="14" height="12"><path d="M1 6l4 4 8-9" stroke="var(--tick)" stroke-width="2.5" fill="none"/></svg>Mobile checkout for pop up sales</li>
    </ul>
  </div>
  <div class="widget archives" style="left:489px;width:200px">
    <h4><span class="widget-icon" style="background:linear-gradient(#e0542a 35%,#cfe4f5 35%)" role="img" aria-label="Calendar icon"></span>Archives</h4>
    <ul>
      <li><svg width="14" height="12"><path d="M1 6l4 4 8-9" stroke="var(--tick)" stroke-width="2.5" fill="none"/></svg>March 2012</li>
      <li><svg width="14" height="12"><path d="M1 6l4 4 8-9" stroke="var(--tick)" stroke-width="2.5" fill="none"/></svg>February 2012</li>
      <li><svg width="14" height="12"><path d="M1 6l4 4 8-9" stroke="var(--tick)" stroke-width="2.5" fill="none"/></svg>January 2012</li>
      <li><svg width="14" height="12"><path d="M1 6l4 4 8-9" stroke="var(--tick)" stroke-width="2.5" fill="none"/></svg>December 2011</li>
      <li><svg width="14" height="12"><path d="M1 6l4 4 8-9" stroke="var(--tick)" stroke-width="2.5" fill="none"/></svg>November 2011</li>
      <li><svg width="14" height="12"><path d="M1 6l4 4 8-9" stroke="var(--tick)" stroke-width="2.5" fill="none"/></svg>October 2011</li>
    </ul>
  </div>
  <div class="widget" style="left:786px;width:250px">
    <h4><span class="widget-icon" style="border-radius:50%;background:#3fa9e0"></span>Chirpnest</h4>
    <div class="chirp-box">New today: post your latest thrift finds straight to Pixelyard from the Tagwell app. Now in five languages.</div>
  </div>
</footer>

<div class="bottom-bar">
  <p class="copyright">© Copyright 2012 tagwell. All Right Reserved</p>
  <div class="social">
    <span style="background:#4a67a8"></span><span style="background:#2f4d6b"></span><span style="background:#eee"></span><span style="background:#1e9fc8"></span><span style="background:#ddd"></span><span style="background:#f08a1c"></span>
  </div>
</div>
</body>
</html>
```